TLB Feedback sticker

We need a sticker design for our secondary school (aged 11 - 18). This is to allow teachers to provide feedback to students and vice-versa, having a conversation with the learner. I would love to have at least two different designs and it to be attractive, so that all can be included. I've attached the basic outline with the information to be presented. It should be A5 size, so that 2 of these can be fitted in.

Target Market(s)

Secondary school students

Industry/Entity Type

School

Font styles to use
Sans Serif

Requirements
Must have
• Attached details of the headings and enough space for all parties to respond.
Should not have
• Anything deemed inappropriate for secondary students

```html
<!DOCTYPE html>
<html lang="en">
<head>
<meta charset="utf-8">
<title>Formative Feedback Stickers</title>
<link rel="stylesheet" href="https://fonts.googleapis.com/css2?family=Oswald:wght@600&family=Open+Sans:wght@400&display=swap">
<style>
  :root {
    --backdrop: #767574;
    --ink: #2a2a2a;
    --rule: #7d7d7d;
    --box-rule: #9a9a9a;
    --white: #ffffff;
    --blue: #0f5ea8;
    --blue-dark: #0b4a88;
    --peach-light: #fff6ee;
    --peach: #f7d8bd;
    --green: #8cc63f;
    --green-dark: #1e9a3a;
    --grey: #dcdcdc;
  }
  * { box-sizing: border-box; margin: 0; padding: 0; }
  html, body { width: 1200px; height: 1000px; overflow: hidden; }
  body {
    background: var(--backdrop);
    font-family: "Open Sans", Arial, sans-serif;
    color: var(--ink);
    position: relative;
  }
  .sticker { position: absolute; overflow: hidden; }
  .sticker--star {
    left: 65px; top: 55px; width: 670px; height: 485px;
    background: radial-gradient(ellipse at 55% 40%, var(--peach-light) 0%, var(--peach) 75%, #f4c9a6 100%);
  }
  .sticker--smile {
    left: 485px; top: 468px; width: 655px; height: 475px;
    background: radial-gradient(ellipse at 50% 40%, var(--white) 0%, #efefef 60%, var(--grey) 100%);
    border: 3px solid var(--green);
  }
  .decoration { position: absolute; pointer-events: none; }
  .sticker--star .decoration {
    left: 170px; top: 25px; width: 300px; height: 290px;
    border-radius: 50%;
    background: radial-gradient(circle, rgba(240,185,140,0.55) 0%, rgba(240,185,140,0.25) 55%, rgba(240,185,140,0) 72%);
  }
  .sticker--smile .decoration {
    left: 228px; top: 60px; width: 196px; height: 196px;
    border-radius: 50%;
    background: radial-gradient(circle, rgba(200,200,200,0.55) 0%, rgba(210,210,210,0.45) 70%, rgba(220,220,220,0) 100%);
  }
  .title-tab {
    position: absolute; left: 0; top: 8px;
    height: 48px; width: 272px;
    font-family: "Oswald", "Arial Narrow", sans-serif;
    font-weight: 600; font-size: 27px; line-height: 48px;
    color: var(--white); padding-left: 38px;
    letter-spacing: 0.2px;
  }
  .sticker--star .title-tab {
    left: 14px; top: 20px; width: 250px; padding-left: 14px;
    background: linear-gradient(180deg, var(--blue) 0%, var(--blue-dark) 100%);
  }
  .sticker--smile .title-tab {
    background: linear-gradient(90deg, var(--green-dark) 0%, var(--green) 100%);
  }
  .meta { position: absolute; font-size: 15px; }
  .meta--teacher { left: 290px; top: 21px; }
  .meta--date { left: 475px; top: 23px; display: flex; align-items: flex-end; }
  .meta--date .blank { display: inline-block; width: 125px; border-bottom: 1px solid var(--rule); margin-left: 2px; height: 16px; }
  .sticker--star .meta--teacher { left: 280px; top: 38px; }
  .sticker--star .meta--date { left: 470px; top: 30px; }

  .field-label { position: absolute; left: 20px; font-size: 13.5px; }
  .rule { position: absolute; left: 20px; right: 12px; border-bottom: 1px solid var(--rule); }
  .tick { position: absolute; left: 14px; width: 15px; height: 13px; }
  .tick path { fill: none; stroke-width: 3.2; stroke-linecap: round; stroke-linejoin: round; }
  .sticker--smile .tick path { stroke: var(--green); }
  .sticker--star .tick path { stroke: var(--blue); }

  .reply-box {
    position: absolute; top: 280px; height: 182px; width: 303px;
    background: var(--white); border-radius: 12px;
    padding: 10px 6px 0 8px;
  }
  .sticker--smile .reply-box { border: 1px solid var(--green); }
  .reply-box--student { left: 15px; }
  .reply-box--teacher { left: 330px; width: 304px; }
  .sticker--star .reply-box { top: 290px; height: 180px; width: 310px; border-radius: 14px; }
  .sticker--star .reply-box--student { left: 25px; }
  .sticker--star .reply-box--teacher { left: 345px; }
  .reply-box h3 { font-weight: 400; font-size: 13.5px; margin-bottom: 8px; }
  .reply-lines { list-style: none; }
  .reply-lines li { height: 28px; border-bottom: 1px solid var(--box-rule); }
  .reply-lines li:first-child { height: 20px; }
</style>
</head>
<body>

<section class="sticker sticker--star" aria-label="Formative feedback sticker, peach design">
  <div class="decoration" role="img" aria-label="Large faint star decoration"></div>
  <h2 class="title-tab">Formative Feedback</h2>
  <p class="meta meta--teacher">Teacher C/L or H/L</p>
  <p class="meta meta--date">Date:<span class="blank"></span></p>

  <p class="field-label" style="top:82px">Strengths (What Went Well…)</p>
  <span class="rule" style="top:106px"></span>
  <span class="rule" style="top:140px"></span>
  <p class="field-label" style="top:160px">Target (Even Better If…)</p>
  <svg class="tick" style="top:186px" viewBox="0 0 15 13" aria-hidden="true"><path d="M2 7 L6 11 L13 2"/></svg>
  <span class="rule" style="top:196px; left:34px"></span>
  <svg class="tick" style="top:216px" viewBox="0 0 15 13" aria-hidden="true"><path d="M2 7 L6 11 L13 2"/></svg>
  <span class="rule" style="top:226px; left:34px"></span>
  <p class="field-label" style="top:236px; left:34px">Action</p>
  <span class="rule" style="top:268px"></span>

  <div class="reply-box reply-box--student">
    <h3>Response (from the student):</h3>
    <ul class="reply-lines"><li></li><li></li><li></li><li></li><li></li></ul>
  </div>
  <div class="reply-box reply-box--teacher">
    <h3>Response and reflection (from the teacher):</h3>
    <ul class="reply-lines"><li></li><li></li><li></li><li></li><li></li></ul>
  </div>
</section>

<section class="sticker sticker--smile" aria-label="Formative feedback sticker, green design">
  <div class="decoration" role="img" aria-label="Large faint round decoration"></div>
  <h2 class="title-tab">Formative Feedback</h2>
  <p class="meta meta--teacher">Teacher C/L or H/L</p>
  <p class="meta meta--date">Date:<span class="blank"></span></p>

  <p class="field-label" style="top:63px">Strengths (What Went Well…)</p>
  <span class="rule" style="top:96px"></span>
  <span class="rule" style="top:129px"></span>
  <p class="field-label" style="top:137px">Target (Even Better If…)</p>
  <svg class="tick" style="top:163px" viewBox="0 0 15 13" aria-hidden="true"><path d="M2 7 L6 11 L13 2"/></svg>
  <span class="rule" style="top:172px; left:34px"></span>
  <svg class="tick" style="top:195px" viewBox="0 0 15 13" aria-hidden="true"><path d="M2 7 L6 11 L13 2"/></svg>
  <span class="rule" style="top:205px; left:34px"></span>
  <p class="field-label" style="top:212px">Action</p>
  <span class="rule" style="top:252px"></span>

  <div class="reply-box reply-box--student">
    <h3>Response (from the student):</h3>
    <ul class="reply-lines"><li></li><li></li><li></li><li></li><li></li></ul>
  </div>
  <div class="reply-box reply-box--teacher">
    <h3>Response and reflection (from the teacher):</h3>
    <ul class="reply-lines"><li></li><li></li><li></li><li></li><li></li></ul>
  </div>
</section>

</body>
</html>
```